Hallowmere Business Card

This is the personal business card for Dr Glen Hallowmere and convers three area of his professional activity - all of them involve (foreign) languages:
o RQVB International Ltd - A translation company with 50 staff. Trades internationally
o TideLatch Ltd - a global online auction marketplace for translation services (startup)
o Vowelcraft - cutting edge technology from the brain sciences which helps learners assimilate the sound patterns of a new language (startup)

Target Market(s)

The card needs to have a "cutting edge" feel - but for a fairly conservative audience - academics, investors.

Industry/Entity Type

Business

Requirements
Must have
• Text:
Dr Glen Hallowmere

Co-founder RQVB International Ltd (Language translation)
Founder TideLatch Ltd (Translation marketplace)
Founder Vowelcraft (Language acquisition)

email: glen.morrow@lintmail.example
Phone: +64 21 555 3916
Twitter: @GlenMorrow4

```html
<!DOCTYPE html>
<html lang="en">
<head>
<meta charset="utf-8">
<title>Dr. Glen Hallowmere – Business Card</title>
<link rel="stylesheet" href="https://fonts.googleapis.com/css2?family=Comic+Neue:wght@400;700&family=Fredoka:wght@600&family=PT+Sans:wght@700&display=swap">
<style>
  :root {
    --paper: #ffffff;
    --ink: #000000;
    --sun: #f7c600;
    --sun-soft: #fbe58a;
    --signal: #e8000b;
    --name-blue: #1f3a93;
    --mist: #f3f3f3;
    --dot-tone: #4a4a4a;
  }
  html, body {
    margin: 0;
    padding: 0;
    overflow: hidden;
    background: var(--paper);
  }
  .card {
    position: relative;
    width: 1200px;
    height: 686px;
    overflow: hidden;
    background: var(--paper);
    color: var(--ink);
  }
  .card-shapes {
    position: absolute;
    inset: 0;
    width: 1200px;
    height: 686px;
  }
  .placeholder { position: absolute; }
  .emblem-area {
    left: 23px; top: 59px; width: 91px; height: 105px;
    background: var(--signal);
  }
  .dots-left-area {
    left: 41px; top: 98px; width: 214px; height: 136px;
    background: linear-gradient(135deg, rgba(74,74,74,0.25), rgba(74,74,74,0.15));
  }
  .dots-right-area {
    left: 1013px; top: 90px; width: 155px; height: 92px;
    background: rgba(74,74,74,0.2);
  }
  .dots-row-area {
    left: 860px; top: 252px; width: 300px; height: 16px;
    background: rgba(74,74,74,0.2);
  }
  .bubble-area {
    left: 270px; top: 46px; width: 915px; height: 205px;
    border-radius: 100px;
    background: var(--mist);
  }
  .trail-area {
    left: 519px; top: 451px; width: 202px; height: 48px;
    background: linear-gradient(170deg, var(--sun-soft), var(--sun));
    opacity: 0.7;
  }
  .headline {
    position: absolute;
    left: 330px;
    top: 122px;
    margin: 0;
    font-family: "Fredoka", "Arial Rounded MT Bold", sans-serif;
    font-weight: 600;
    font-size: 60px;
    line-height: 1;
    letter-spacing: 2px;
    color: var(--name-blue);
    -webkit-text-stroke: 1.4px var(--ink);
    transform: rotate(-5deg);
    transform-origin: left center;
    white-space: nowrap;
  }
  .ventures {
    position: absolute;
    left: 644px;
    top: 296px;
    margin: 0;
    padding: 0;
    list-style: none;
    font-family: "Comic Neue", "Comic Sans MS", cursive;
    font-weight: 700;
    font-size: 16px;
    line-height: 1;
  }
  .ventures li { height: 49px; white-space: nowrap; }
  .holder {
    position: absolute;
    left: 96px;
    top: 497px;
    font-family: "PT Sans", Verdana, sans-serif;
    font-weight: 700;
  }
  .holder-name {
    margin: 0;
    font-size: 34px;
    letter-spacing: 1px;
    line-height: 1;
  }
  .holder-title {
    margin: 10px 0 0;
    font-size: 26px;
    letter-spacing: 1.5px;
    line-height: 1;
  }
  .contact {
    position: absolute;
    left: 644px;
    top: 502px;
    margin: 0;
    font-family: "Comic Neue", "Comic Sans MS", cursive;
    font-size: 31px;
    line-height: 50px;
    font-style: normal;
    white-space: nowrap;
  }
  .contact p { margin: 0; }
</style>
</head>
<body>
<main class="card">
  <svg class="card-shapes" viewBox="0 0 1200 686" aria-hidden="true">
    <polygon class="band" points="96,87 1166,73 1157,228 132,255" fill="var(--sun)"/>
    <polygon class="pointer" points="34,505 87,521 34,537" fill="var(--signal)"/>
  </svg>

  <div class="placeholder dots-left-area" role="img" aria-label="Cluster of small black dots"></div>
  <div class="placeholder dots-right-area" role="img" aria-label="Cluster of small black dots"></div>
  <div class="placeholder dots-row-area" role="img" aria-label="Row of small black dots"></div>
  <div class="placeholder emblem-area" role="img" aria-label="Red and white target emblem on a black square"></div>
  <div class="placeholder bubble-area" role="img" aria-label="White speech bubble with black outline framing the name"></div>
  <div class="placeholder trail-area" role="img" aria-label="Curved trail of yellow dots"></div>

  <h1 class="headline">Dr. Glen Hallowmere</h1>

  <ul class="ventures">
    <li>Co-founder RQVB International Ltd (Language Translation)</li>
    <li>Founder TideLatch Ltd (Translation Marketplace)</li>
    <li>Founder Vowelcraft (Language Acquisition)</li>
  </ul>

  <div class="holder">
    <p class="holder-name">Glen Hallowmere</p>
    <p class="holder-title">Profession in Foreign Languages</p>
  </div>

  <address class="contact">
    <p>Phone: +64 21 555 3916</p>
    <p>Twitter: @GlenMorrow4</p>
    <p>E-mail: glen.morrow@lintmail.example</p>
  </address>
</main>
</body>
</html>
```